Hallowmere Business Card

This is the personal business card for Dr Glen Hallowmere and convers three area of his professional activity - all of them involve (foreign) languages:
o RQVB International Ltd - A translation company with 50 staff. Trades internationally
o TideLatch Ltd - a global online auction marketplace for translation services (startup)
o Vowelcraft - cutting edge technology from the brain sciences which helps learners assimilate the sound patterns of a new language (startup)

Target Market(s)

The card needs to have a "cutting edge" feel - but for a fairly conservative audience - academics, investors.

Industry/Entity Type

Business

Requirements
Must have
• Text:
Dr Glen Hallowmere

Co-founder RQVB International Ltd (Language translation)
Founder TideLatch Ltd (Translation marketplace)
Founder Vowelcraft (Language acquisition)

email: glen.morrow@lintmail.example
Phone: +64 21 555 3916
Twitter: @GlenMorrow4

```html
<!DOCTYPE html>
<html lang="en">
<head>
<meta charset="utf-8">
<title>Hallowmere Business Card</title>
<link rel="stylesheet" href="https://fonts.googleapis.com/css2?family=Bebas+Neue&display=swap">
<style>
  :root {
    --stage: #3a3a3a;
    --paper: #ffffff;
    --ink: #111111;
    --accent: #4a86c8;
    --grad-start: #3f7fcd;
    --grad-end: #42bcc8;
    --photo-light: #f1f3f6;
    --photo-mid: #e3e8ee;
  }
  * { margin: 0; padding: 0; box-sizing: border-box; }
  html, body {
    width: 1200px; height: 534px; overflow: hidden;
    background: var(--stage);
    font-family: "Bebas Neue", "Arial Narrow", sans-serif;
  }
  .canvas { position: relative; width: 1200px; height: 534px; }
  .card {
    position: absolute; top: 119px; width: 517px; height: 295px; overflow: hidden;
  }
  .card--front { left: 62px; background: var(--paper); }
  .card--back {
    left: 622px;
    background: linear-gradient(135deg, var(--grad-start) 0%, var(--grad-start) 30%, var(--grad-end) 100%);
    display: flex; flex-direction: column; align-items: center; justify-content: center;
    padding-bottom: 18px;
  }
  .portrait-area {
    position: absolute; left: 0; top: 0; width: 403px; height: 295px;
    background: radial-gradient(ellipse at 40% 45%, var(--photo-mid) 0%, var(--photo-light) 55%, var(--paper) 100%);
    opacity: .8;
  }
  .accent-band {
    position: absolute; right: 0; top: 0; width: 114px; height: 295px;
    background: linear-gradient(160deg, var(--grad-start) 0%, var(--grad-start) 45%, var(--grad-end) 100%);
  }
  .front-text {
    position: absolute; right: 144px; top: 0; text-align: right; width: 380px;
  }
  .front-name {
    position: absolute; right: 0; top: 53px;
    font-size: 41px; line-height: 1; color: var(--accent); letter-spacing: .2px; white-space: nowrap;
  }
  .contact {
    position: absolute; right: 0; top: 163px; list-style: none;
    font-size: 13.5px; line-height: 15.5px; color: var(--ink); white-space: nowrap;
  }
  .roles {
    position: absolute; right: 0; top: 225px; list-style: none;
    font-size: 13.5px; line-height: 15.5px; color: var(--ink); white-space: nowrap;
  }
  .label, .company { color: var(--accent); }
  .label { font-size: 11.5px; }
  .back-name {
    font-size: 55px; line-height: 1; color: var(--paper); letter-spacing: .3px;
  }
  .back-ventures {
    margin-top: 6px; list-style: none; display: flex;
    font-size: 11.5px; color: var(--paper); letter-spacing: .4px;
  }
  .back-ventures li + li::before {
    content: "|"; margin: 0 7px; opacity: .7;
  }
</style>
</head>
<body>
<main class="canvas">
  <section class="card card--front">
    <div class="portrait-area" role="img" aria-label="Faded photograph of a doctor in a white coat with a stethoscope, arms folded"></div>
    <div class="accent-band"></div>
    <div class="front-text">
      <h1 class="front-name">Dr Glen Hallowmere</h1>
      <ul class="contact">
        <li><span class="label">Email:</span> glen.morrow@lintmail.example</li>
        <li><span class="label">Phone:</span> +64 21 555 3916</li>
        <li><span class="label">Twitter:</span> @GlenMorrow4</li>
      </ul>
      <ul class="roles">
        <li>Co-founder <span class="company">RQVB International Ltd</span> (Language translation)</li>
        <li>Founder <span class="company">TideLatch Ltd</span> (Translation marketplace)</li>
        <li>Founder <span class="company">Vowelcraft</span> (Language acquisition)</li>
      </ul>
    </div>
  </section>

  <section class="card card--back">
    <h2 class="back-name">Dr Glen Hallowmere</h2>
    <ul class="back-ventures">
      <li>RQVB International Ltd</li>
      <li>TideLatch Ltd</li>
      <li>Vowelcraft</li>
    </ul>
  </section>
</main>
</body>
</html>
```